I need a flyer made , the flyer can be one page or two pages or three pages . I will be posting this on Instagram and social media platforms. I am a luxury home builder , I am looking to hire a construction project manager . Below are some examples and ideas what can be on the flyer

We’re looking for a construction project manager who’s passionate about building luxury homes at the highest standards
We’re hiring construction project manager
* Experience 5+ years in residential project management with a strong portfolio of completed homes.
* location : Bergen County NJ
* excellent leadership skills, leads teams with confidence and clarity
* communicates seamlessly with architects , engineers, designers and clients
*knows how to manage budgets and timelines without compromising quality
*solves problems with a positive solution first mindset
* pays attention to every detail because in luxury the small things are the big things

Apply now , link in bio or DM to connect.

My logo is attached, my web site www.ridgelanebuilders.com
My style is modern but still warm and inviting. I like a clean classy look .
Updates

Please don’t add any images of chairs or people to the flyer , I do not want people on my flyer. Do not add standard images of offices and houses , we are luxury builders , we build homes over 2 million dollars. Keep a classy , simple modern look . High end .

You can add a white hard hat with my logo on it for a image , this is a suggestion does not have to be on my flyer ,

```html
<!DOCTYPE html>
<html lang="en">
<head>
<meta charset="utf-8">
<title>Ridgelane Builders – We're Hiring</title>
<link rel="stylesheet" href="https://fonts.googleapis.com/css2?family=Archivo+Black&family=Montserrat:wght@400;500;700&family=Nunito+Sans:wght@300;400&family=Cormorant+Garamond:wght@500&display=swap">
<style>
  :root {
    --yellow: #f1cb1f;
    --ink: #111111;
    --grey: #e3e4e6;
    --paper: #ffffff;
    --text: #1c1c1c;
    --art: #d9b41a;
  }
  html, body {
    margin: 0;
    padding: 0;
    overflow: hidden;
    background: var(--paper);
  }
  .flyer {
    position: relative;
    width: 960px;
    height: 1200px;
    overflow: hidden;
    background: var(--paper);
    font-family: "Nunito Sans", sans-serif;
    color: var(--text);
  }
  .decor, .titles {
    position: absolute;
    left: 0;
    top: 0;
    width: 960px;
    height: 1200px;
  }
  .megaphone-art {
    position: absolute;
    left: 0;
    top: 170px;
    width: 270px;
    height: 360px;
    background: var(--art);
    border-radius: 0 48% 48% 0;
  }
  .brand {
    position: absolute;
    left: 698px;
    top: 48px;
    width: 262px;
    height: 105px;
    background: var(--ink);
    color: var(--paper);
    display: flex;
    flex-direction: column;
    align-items: center;
    justify-content: center;
    font-family: "Cormorant Garamond", serif;
    font-weight: 500;
    font-size: 34px;
    line-height: 1.05;
    letter-spacing: 1px;
    text-align: center;
  }
  .headline-word {
    font-family: "Archivo Black", sans-serif;
    fill: var(--ink);
  }
  .role-line {
    font-family: "Montserrat", sans-serif;
    font-weight: 700;
    fill: var(--yellow);
  }
  .intro {
    position: absolute;
    left: 198px;
    top: 520px;
    margin: 0;
    font-size: 24px;
    line-height: 30px;
    font-weight: 300;
    color: var(--yellow);
    text-transform: uppercase;
  }
  .requirements {
    position: absolute;
    left: 0;
    top: 0;
    margin: 0;
    padding: 0;
    list-style: none;
    font-size: 16.2px;
    font-weight: 400;
    text-transform: uppercase;
    color: var(--text);
  }
  .requirement {
    position: absolute;
    left: 138px;
    white-space: nowrap;
    line-height: 26px;
    text-indent: 18px;
  }
  .requirement::before {
    content: "";
    position: absolute;
    left: -44px;
    top: 2px;
    width: 16px;
    height: 16px;
    border: 3px solid var(--yellow);
    border-radius: 50%;
    background: radial-gradient(circle, var(--yellow) 0 4px, transparent 5px);
  }
  .call {
    position: absolute;
    left: 36px;
    top: 1044px;
    font-family: "Montserrat", sans-serif;
    font-size: 19px;
    line-height: 22px;
    letter-spacing: 2px;
  }
  .call-label {
    color: var(--yellow);
    font-weight: 700;
    display: block;
    margin-bottom: 6px;
  }
  .call-text {
    color: var(--ink);
    font-weight: 500;
    display: block;
  }
  .website {
    position: absolute;
    left: 310px;
    top: 1088px;
    font-family: "Montserrat", sans-serif;
    font-size: 16px;
    letter-spacing: 2px;
    color: var(--ink);
  }
  .accent-bar {
    position: absolute;
    left: 643px;
    top: 1082px;
    width: 317px;
    height: 34px;
    background: var(--yellow);
  }
</style>
</head>
<body>
<main class="flyer">
  <svg class="decor" viewBox="0 0 960 1200" aria-hidden="true">
    <circle class="sun-circle" cx="174" cy="89" r="404" fill="var(--yellow)"/>
    <circle class="mist-circle" cx="889" cy="359" r="108" fill="var(--grey)"/>
    <path class="corner-curve" d="M0 974 C110 950 215 990 260 1080 L283 1150 L341 1172 L350 1200" fill="none" stroke="var(--yellow)" stroke-width="6"/>
  </svg>

  <div class="megaphone-art" role="img" aria-label="Black line illustration of a megaphone with sound lines"></div>

  <div class="brand">
    <span class="brand-name">RIDGELANE</span>
    <span class="brand-sub">BUILDERS</span>
  </div>

  <svg class="titles" viewBox="0 0 960 1200">
    <title>We're hiring: Construction Project Manager</title>
    <text class="headline-word headline-were" x="0" y="0" font-size="92" textLength="330" lengthAdjust="spacingAndGlyphs" transform="translate(320 273) rotate(-21)">WE’RE</text>
    <text class="headline-word headline-hiring" x="0" y="0" font-size="140" textLength="505" lengthAdjust="spacingAndGlyphs" transform="translate(288 394) rotate(-17)">HIRING</text>
    <text class="role-line role-construction" x="0" y="0" font-size="41" textLength="348" lengthAdjust="spacingAndGlyphs" transform="translate(488 402) rotate(-19)">CONSTRUCTION</text>
    <text class="role-line role-manager" x="0" y="0" font-size="41" textLength="430" lengthAdjust="spacingAndGlyphs" transform="translate(502 454) rotate(-19)">PROJECT MANAGER</text>
  </svg>

  <p class="intro">We’re looking for a construction project manager<br>who’s passionate about building luxury homes<br>at the highest standards</p>

  <ul class="requirements">
    <li class="requirement" style="top:636px">Experience 5+ years in residential project management with a strong<br>portfolio of completed homes.</li>
    <li class="requirement" style="top:703px">Location : Bergen County NJ</li>
    <li class="requirement" style="top:741px">Excellent leadership skills, leads teams with confidence and clarity</li>
    <li class="requirement" style="top:779px">Communicates seamlessly with architects , engineers, designers and clients</li>
    <li class="requirement" style="top:817px">Knows how to manage budgets and timelines without compromising quality</li>
    <li class="requirement" style="top:855px">Solves problems with a positive solution first mindset</li>
    <li class="requirement" style="top:898px">Pays attention to every detail because in luxury the small things are<br>the big things</li>
  </ul>

  <div class="call">
    <span class="call-label">APPLY NOW</span>
    <span class="call-text">link in bio or<br>DM to connect.</span>
  </div>

  <div class="website">www.ridgelanebuilders.com</div>
  <div class="accent-bar"></div>
</main>
</body>
</html>
```